Media Browser and player web application

I need to redesign a web application that enables to browse a media server (Tellavo) contents (images, audio, video) and play it in a web player.

Current implementation of the application can be seen at: http://www.tellavohub.example/content/demonstration-tellavo-pro-online-media-browser

This refresh is aiming to:
1) make the application simpler, based on typology (think Windows Metro style, VidSpire, Flickora); a simple fan concept is here: http://dex.lomarquin.example/tellavo/
2) make the application work on desktop as well as touch screen devices (ie no hover functionality, no pagination, large touch controls)
3) fast (remove unnecessary animations)
4) design with the app being responsive in mind

The attached UX designs show the basic flows in the application. Please note that the placement of controls (for example) is not set in stone and I welcome your input on the layout.

Ideally the default theme will be dark. Items' thumbnails will be square place holders, with images fit in them depending on the item icons' aspect ratio.

Also attaching the product's logo (Tellavo) and icon. The web application's name is ClipRover (or Tellavo ClipRover), so it should be included in the design (the UX designs include place holder Tellavo logo in the left top corner).

The main categories for each file type are (you will have to provide an icon for each of these):
- Audio: Albums, Artists, Album artists, Folders, Genres, Composers, Titles, Random music, Random albums, Last listened, Playlists, Online
- Image: Albums, Folders, Year, Month, Playlists, Online
- Video: Titles, Movies, Series, Folders, Last viewed, Last added, Genres, Actors, Directors, Producers, Release years, Playlists, Online
Updates

Target Market(s)

Mostly tech enthusiasts who want to stream their media over the internet to their devices.

Industry/Entity Type

Artists

Requirements
Must have
• Designs for all the provided UX designs
Touch-friendly web application design
High-res (Retina) assets
Light, type based Metro-like design
Nice to have
• Responsive web version
Dark and Light theme switching.
Should not have
• Chrome
Heavy graphics (eg backgrounds) that take time to load

```html
<!DOCTYPE html>
<html lang="en">
<head>
<meta charset="utf-8">
<title>Tellavo ClipRover – Audio</title>
<link rel="stylesheet" href="https://fonts.googleapis.com/css2?family=Raleway:wght@500;700&family=Questrial&display=swap">
<style>
  :root{
    --bg-center:#2b5c84;
    --bg-edge:#0d2c4b;
    --accent:#3596db;
    --accent-dark:#2a7fc0;
    --tile-band:#3e4451;
    --panel:#e6ebf1;
    --panel-text:#a9b0b8;
    --title-text:#2e3440;
    --tool:#3e4451;
    --tool-icon:#aab3bd;
    --white:#ffffff;
  }
  *{box-sizing:border-box;margin:0;padding:0}
  html,body{width:1200px;height:1000px;overflow:hidden}
  body{
    position:relative;
    font-family:"Raleway",sans-serif;
    background:radial-gradient(ellipse 75% 70% at 50% 45%,var(--bg-center) 0%,#22507a 55%,var(--bg-edge) 100%);
  }
  .brand{
    position:absolute;left:78px;top:0;width:276px;height:160px;
    background:var(--accent);
    box-shadow:10px 6px 0 #24394f;
    display:flex;align-items:center;justify-content:center;
  }
  .brand-name{font-family:"Raleway",sans-serif;font-weight:700;font-size:54px;color:var(--white);letter-spacing:1px}
  .toolbar{position:absolute;left:908px;top:156px;display:flex;gap:13px}
  .tool{width:54px;height:54px;background:var(--tool);display:flex;flex-direction:column;align-items:center;justify-content:center;gap:3px;color:var(--white);font-size:7px;font-weight:700;letter-spacing:.2px}
  .section-icon{position:absolute;left:166px;top:236px;width:172px;height:132px;background:var(--accent);display:flex;align-items:center;justify-content:center}
  .section-info{position:absolute;left:352px;top:236px;width:675px;height:132px;background:var(--panel);border-left:12px solid var(--accent);padding:12px 24px 0 13px}
  .section-head{display:flex;align-items:center;gap:10px}
  .section-badge{width:27px;height:27px;background:var(--accent);display:flex;align-items:center;justify-content:center}
  .section-title{font-family:"Questrial",sans-serif;font-size:18px;color:var(--title-text);margin-top:6px}
  .section-text{font-family:"Questrial",sans-serif;font-size:12px;line-height:13px;color:var(--panel-text);margin:10px 0 0 4px;height:52px;overflow:hidden;text-align:justify}
  .categories{position:absolute;left:165px;top:393px;display:grid;grid-template-columns:repeat(4,186px);column-gap:40px;row-gap:41px}
  .tile{position:relative;width:186px;height:241px}
  .tile-art{position:absolute;left:0;top:0;width:186px;height:141px;background:linear-gradient(160deg,#6f9ac0 0%,#4f7ca6 45%,#2f5a85 100%)}
  .tile-band{position:absolute;left:0;top:141px;width:186px;height:79px;background:var(--tile-band)}
  .tile-base{position:absolute;left:0;top:220px;width:186px;height:21px;background:var(--accent)}
  .tile-icon{position:absolute;left:61px;top:108px;width:62px;height:62px;background:var(--accent);display:flex;align-items:center;justify-content:center}
  .tile-label{position:absolute;left:0;top:184px;width:186px;text-align:center;color:var(--white);font-size:17px;font-weight:500}
</style>
</head>
<body>
  <header>
    <div class="brand"><span class="brand-name">Tellavo</span></div>
    <nav class="toolbar">
      <div class="tool">
        <svg width="36" height="24" viewBox="0 0 36 24" fill="var(--tool-icon)"><rect x="0" y="0" width="10" height="10" rx="2"/><rect x="0" y="13" width="10" height="10" rx="2"/><rect x="13" y="1" width="23" height="3"/><rect x="13" y="7" width="23" height="3"/><rect x="13" y="14" width="23" height="3"/><rect x="13" y="20" width="23" height="3"/></svg>
        <span>QUEUE</span>
      </div>
      <div class="tool">
        <svg width="26" height="26" viewBox="0 0 26 26"><circle cx="10" cy="10" r="7" fill="none" stroke="var(--tool-icon)" stroke-width="3"/><line x1="15" y1="15" x2="23" y2="23" stroke="var(--tool-icon)" stroke-width="4" stroke-linecap="round"/></svg>
        <span>SEARCH</span>
      </div>
    </nav>
  </header>

  <main>
    <div class="section-icon">
      <svg width="120" height="86" viewBox="0 0 120 86" fill="none" stroke="var(--white)" stroke-width="10" stroke-linecap="round"><path d="M10 68 V50 A50 46 0 0 1 110 50 V68"/><line x1="28" y1="55" x2="28" y2="80"/><line x1="92" y1="55" x2="92" y2="80"/><rect x="4" y="56" width="12" height="26" rx="6" fill="var(--white)" stroke="none"/><rect x="104" y="56" width="12" height="26" rx="6" fill="var(--white)" stroke="none"/></svg>
    </div>
    <section class="section-info">
      <div class="section-head">
        <div class="section-badge"><svg width="13" height="11" viewBox="0 0 13 11" fill="none" stroke="#fff" stroke-width="2"><path d="M2 10 V6 A4.5 4.5 0 0 1 11 6 V10"/></svg></div>
        <h1 class="section-title">Audio</h1>
      </div>
      <p class="section-text">Place your description here. Audio Description, also called Video Description, refers to an additional narration track intended primarily for blind and visually impaired consumers of visual media (including television and film, dance, opera, and visual art). It consists of a narrator talking through the presentation, describing what is happening on the screen or stage during the natural pauses in the</p>
    </section>

    <div class="categories">
      <div class="tile"><div class="tile-art" role="img" aria-label="Abstract blue geometric backdrop"></div><div class="tile-band"></div><div class="tile-base"></div>
        <div class="tile-icon"><svg width="36" height="36" viewBox="0 0 36 36" fill="#fff"><circle cx="18" cy="11" r="7"/><path d="M4 34 C4 22 10 19 18 19 C26 19 32 22 32 34 Z"/></svg></div>
        <div class="tile-label">ARTISTS</div></div>
      <div class="tile"><div class="tile-art" role="img" aria-label="Abstract blue geometric backdrop"></div><div class="tile-band"></div><div class="tile-base"></div>
        <div class="tile-icon"><svg width="46" height="36" viewBox="0 0 46 36"><path d="M2 4 H16 L19 8 H40 V34 H2 Z" fill="none" stroke="#fff" stroke-width="3"/><path d="M8 13 H44 L40 34 H3 Z" fill="#fff"/><circle cx="24" cy="19" r="4" fill="var(--accent)"/><path d="M16 31 C16 25 19 24 24 24 C29 24 32 25 32 31 Z" fill="var(--accent)"/></svg></div>
        <div class="tile-label">ALBUM ARTISTS</div></div>
      <div class="tile"><div class="tile-art" role="img" aria-label="Abstract blue geometric backdrop"></div><div class="tile-band"></div><div class="tile-base"></div>
        <div class="tile-icon"><svg width="46" height="36" viewBox="0 0 46 36"><path d="M2 4 H16 L19 8 H40 V34 H2 Z" fill="none" stroke="#fff" stroke-width="3"/><path d="M8 13 H44 L40 34 H3 Z" fill="#fff"/><path d="M20 29 V18 L32 16 V27" fill="none" stroke="var(--accent)" stroke-width="2"/><circle cx="18" cy="29" r="3" fill="var(--accent)"/><circle cx="30" cy="27" r="3" fill="var(--accent)"/></svg></div>
        <div class="tile-label">FOLDERS</div></div>
      <div class="tile"><div class="tile-art" role="img" aria-label="Abstract blue geometric backdrop"></div><div class="tile-band"></div><div class="tile-base"></div>
        <div class="tile-icon"><svg width="30" height="38" viewBox="0 0 30 38"><rect x="9" y="2" width="12" height="22" rx="6" fill="#fff"/><path d="M4 17 A11 11 0 0 0 26 17" fill="none" stroke="#fff" stroke-width="3"/><line x1="15" y1="28" x2="15" y2="34" stroke="#fff" stroke-width="3"/><line x1="8" y1="35" x2="22" y2="35" stroke="#fff" stroke-width="3"/></svg></div>
        <div class="tile-label">GENRES</div></div>

      <div class="tile"><div class="tile-art" role="img" aria-label="Abstract blue geometric backdrop"></div><div class="tile-band"></div><div class="tile-base"></div>
        <div class="tile-icon"><svg width="36" height="36" viewBox="0 0 36 36"><path d="M20 6 H6 V30 H30 V16" fill="none" stroke="#fff" stroke-width="3"/><path d="M28 3 L33 8 L19 22 L13 23 L14 17 Z" fill="#fff"/></svg></div>
        <div class="tile-label">COMPOSERS</div></div>
      <div class="tile"><div class="tile-art" role="img" aria-label="Abstract blue geometric backdrop"></div><div class="tile-band"></div><div class="tile-base"></div>
        <div class="tile-icon"><svg width="42" height="30" viewBox="0 0 42 30" fill="#fff"><rect y="0" width="42" height="3"/><rect y="9" width="42" height="3"/><rect y="18" width="42" height="3"/><rect y="27" width="42" height="3"/></svg></div>
        <div class="tile-label">TITLES</div></div>
      <div class="tile"><div class="tile-art" role="img" aria-label="Abstract blue geometric backdrop"></div><div class="tile-band"></div><div class="tile-base"></div>
        <div class="tile-icon"><svg width="36" height="32" viewBox="0 0 36 32" fill="none" stroke="#fff" stroke-width="4"><path d="M4 16 V10 H28"/><path d="M32 16 V22 H8"/><path d="M25 3 L32 10 L25 17 Z" fill="#fff" stroke="none"/><path d="M11 15 L4 22 L11 29 Z" fill="#fff" stroke="none"/></svg></div>
        <div class="tile-label">RANDOM</div></div>
      <div class="tile"><div class="tile-art" role="img" aria-label="Abstract blue geometric backdrop"></div><div class="tile-band"></div><div class="tile-base"></div>
        <div class="tile-icon"><svg width="26" height="38" viewBox="0 0 26 38"><rect x="1" y="1" width="24" height="36" rx="4" fill="#fff"/><rect x="5" y="5" width="16" height="12" fill="var(--accent)"/><circle cx="13" cy="27" r="6" fill="var(--accent)"/><circle cx="13" cy="27" r="2" fill="#fff"/></svg></div>
        <div class="tile-label">PLAYISTS</div></div>
    </div>
  </main>
</body>
</html>
```